12-page Product Brochure for School Archiving Specialist Company

We require a 12-page brochure for our company based in Melbourne, VIC. Our company specializes in tailored archiving solutions for Australian schools of all sizes, and our main product is the "Tidy Vault" archiving system.
We have a ready-to-use brochure structure that can help designers get a better idea of what we're looking for in the final brochure. We will also provide imagery, graphics, and copy that will be used in the brochure - designers will just have to piece them all together and add their own touch of flair to it!
We are looking for the design to clearly communicate what we we do from a product, service and system perspective. The design should inspire trust, be clear and concise, but also to incorporate the fun spirit that embodies our company and our mascots, Pimble and Wexo.
Attached is a suggested brochure structure, previous brochures we have had designed, a project brief, as well as examples of what we like.
Company Name: Tidy Vault (operating under Bramble Files Group)
Company Location: Melbourne, Victoria, Australia
Contacts: perry@bramblefilesgroup.com.au / desmond@bramblefilesgroup.com.au
Project Type: 12-page A4 Brochure
Project Goal: A brochure that clearly communicates what we do from a product, service, and system perspective. The design should inspire trust, be clear and concise, but should also incorporate the fun spirit that embodies our company and our mascots, Pimble and Wex.
Final Output Format: .PDF and .AI or .INDD
Project Details and Scope of Work: We require a 14-page A4 brochure for our company based in Melbourne, VIC. Our company specializes in tailored archiving solutions for Australian schools of all sizes, and our main product is the "Tidy Vault" archiving system. We have a ready-to-use brochure structure that can help designers get a better idea of what we're looking for in the final brochure. We will also provide imagery, graphics, and copy that will be used in the brochure - designers will just have to piece them all together, fill in any gaps, and add their own touch of flair to it!
Links to Existing Content:
Graphics/Imagery*: https://files.example-share.net/folders/a7k2pq91
Brochure Copy:
https://texts.example-share.net/doc/b4m8rz30
Photos:
https://files.example-share.net/folders/c9t3wn57
Previous Tidy Vault Brochures and Best Practice Design Examples Pages**:
https://files.example-share.net/folders/d2h6vx84
* Each folder, named after different sections of the brochure, contains graphics we would like to be used for that corresponding page/section.
** The photos in each folder are examples. Please refer to the Brochure Photo Folder for all options.
Target Market(s)
Schools of all sizes in Australia
Industry/Entity Type
Archiving / Storage
Look and feel

```html
<!DOCTYPE html>
<html lang="en">
<head>
<meta charset="utf-8">
<title>Tidy Vault Brochure Spreads</title>
<link rel="stylesheet" href="https://fonts.googleapis.com/css2?family=Oswald:wght@500;700&family=Open+Sans:wght@400;600;700&display=swap">
<style>
  :root{
    --blue:#1e8fd6;
    --blue-dark:#1566a8;
    --red:#e0272b;
    --green:#2f9a48;
    --ink:#23303d;
    --grey-board:#e8e8e8;
    --paper:#ffffff;
    --rule:#d5d9de;
  }
  *{margin:0;padding:0;box-sizing:border-box}
  html,body{width:1200px;height:3712px;overflow:hidden;background:var(--paper)}
  .board{position:relative;width:1200px;height:3712px}
  .board__stage{position:absolute;left:0;top:0;width:1200px;height:1340px;background:var(--grey-board)}
  .defs{position:absolute;width:0;height:0}
  .thumb{position:absolute;width:420px;height:276px;box-shadow:0 6px 18px rgba(0,0,0,.18)}
  .spread{position:absolute;left:280px;width:640px;height:420px;box-shadow:0 2px 10px rgba(0,0,0,.12)}
  .h{font-family:'Oswald',sans-serif;font-weight:700}
  .hm{font-family:'Oswald',sans-serif;font-weight:500}
  .b{font-family:'Open Sans',sans-serif;font-weight:400}
  .bb{font-family:'Open Sans',sans-serif;font-weight:700}
</style>
</head>
<body>
<div class="board">
  <div class="board__stage"></div>

  <svg class="defs" aria-hidden="true">
    <defs>
      <linearGradient id="g-lockers" x1="0" y1="0" x2="1" y2="1"><stop offset="0" stop-color="#3aa557"/><stop offset="1" stop-color="#1d6e35"/></linearGradient>
      <linearGradient id="g-redgreen" x1="0" y1="0" x2="1" y2="0"><stop offset="0" stop-color="#2f9a48"/><stop offset=".55" stop-color="#c93a32"/><stop offset="1" stop-color="#d94a3d"/></linearGradient>
      <linearGradient id="g-grey" x1="0" y1="0" x2="1" y2="1"><stop offset="0" stop-color="#8b8e92"/><stop offset="1" stop-color="#3e4247"/></linearGradient>
      <linearGradient id="g-boxes" x1="0" y1="0" x2="1" y2="1"><stop offset="0" stop-color="#c9a77c"/><stop offset="1" stop-color="#7b5a3c"/></linearGradient>
      <linearGradient id="g-crates" x1="0" y1="0" x2="1" y2="0"><stop offset="0" stop-color="#e2b23a"/><stop offset=".4" stop-color="#d8473c"/><stop offset="1" stop-color="#2f7fc8"/></linearGradient>
      <linearGradient id="g-fold" x1="0" y1="0" x2="1" y2="0"><stop offset="0" stop-color="#000" stop-opacity="0"/><stop offset="1" stop-color="#000" stop-opacity=".12"/></linearGradient>

      <!-- Cover spread -->
      <symbol id="s-cover" viewBox="0 0 640 420">
        <rect width="640" height="420" fill="#fff"/>
        <rect x="14" y="12" width="10" height="10" fill="var(--red)"/>
        <text x="29" y="21" class="bb" font-size="10" fill="var(--blue)">Tidy Vault</text>
        <rect x="0" y="36" width="320" height="250" fill="url(#g-lockers)" role="img" aria-label="Photo of green school archive lockers"/>
        <rect x="10" y="56" width="180" height="78" fill="var(--blue)"/>
        <text x="20" y="88" class="h" font-size="26" fill="#fff">READY TO</text>
        <text x="20" y="122" class="h" font-size="26" fill="#fff">GET STARTED?</text>
        <rect x="0" y="286" width="320" height="134" fill="var(--blue)"/>
        <circle cx="30" cy="318" r="11" fill="#fff"/>
        <path d="M25 312l3 0 2 4-2 2a8 8 0 0 0 4 4l2-2 4 2 0 3c-7 1-14-6-13-13z" fill="var(--blue)"/>
        <text x="50" y="327" class="h" font-size="24" fill="#fff">1300 555 204</text>
        <text x="20" y="352" class="b" font-size="8" fill="#fff">Book a free archive review for your school today.</text>
        <text x="20" y="364" class="b" font-size="8" fill="#fff">We plan, install and support every stage.</text>
        <text x="20" y="400" class="b" font-size="7" fill="#cfe6f7">perry@bramblefilesgroup.com.au</text>

        <rect x="320" y="0" width="320" height="240" fill="url(#g-redgreen)" role="img" aria-label="Photo of red and green archive lockers"/>
        <rect x="330" y="12" width="78" height="28" fill="#fff"/>
        <rect x="336" y="21" width="10" height="10" fill="var(--red)"/>
        <text x="350" y="30" class="bb" font-size="10" fill="var(--blue)">Tidy Vault</text>
        <rect x="430" y="96" width="200" height="118" fill="var(--blue)"/>
        <text x="442" y="128" class="h" font-size="24" fill="#fff">THE SCHOOL</text>
        <text x="442" y="162" class="h" font-size="30" fill="#fff">ARCHIVE</text>
        <text x="442" y="200" class="h" font-size="30" fill="#fff">SPECIALISTS</text>
        <rect x="320" y="240" width="320" height="180" fill="#fff"/>
        <rect x="336" y="256" width="90" height="60" fill="url(#g-grey)" role="img" aria-label="Photo of archive room"/>
        <rect x="434" y="256" width="90" height="60" fill="url(#g-crates)" role="img" aria-label="Photo of storage crates"/>
        <rect x="532" y="256" width="92" height="60" fill="url(#g-boxes)" role="img" aria-label="Photo of file boxes"/>
        <rect x="320" y="330" width="320" height="90" fill="var(--blue)"/>
        <text x="336" y="360" class="hm" font-size="13" fill="#fff">Tailored archiving for Australian schools</text>
        <text x="336" y="378" class="b" font-size="8" fill="#fff">Melbourne based. Built for schools of all sizes.</text>
        <rect x="318" y="0" width="2" height="420" fill="url(#g-fold)"/>
      </symbol>

      <!-- Table of contents -->
      <symbol id="s-toc" viewBox="0 0 640 420">
        <rect width="640" height="420" fill="#fff"/>
        <rect x="0" y="0" width="320" height="420" fill="url(#g-grey)" role="img" aria-label="Photo of a staff member at grey archive lockers"/>
        <rect x="120" y="210" width="60" height="40" fill="var(--red)" opacity=".85"/>
        <rect x="190" y="210" width="60" height="40" fill="var(--blue)" opacity=".85"/>
        <text x="20" y="404" class="b" font-size="7" fill="#fff">02</text>
        <rect x="344" y="150" width="4" height="48" fill="var(--blue)"/>
        <text x="356" y="170" class="h" font-size="18" fill="var(--ink)">TABLE OF</text>
        <text x="356" y="194" class="h" font-size="18" fill="var(--blue)">CONTENTS</text>
        <rect x="528" y="70" width="90" height="58" rx="3" fill="#2b3644"/>
        <rect x="533" y="75" width="80" height="46" fill="#dfe9f3" role="img" aria-label="Screen showing archive software"/>
        <rect x="566" y="128" width="14" height="10" fill="#2b3644"/>
        <g class="b" font-size="8" fill="var(--ink)">
          <text x="356" y="226">Introduction</text><text x="600" y="226">03</text>
          <text x="356" y="246">The Problem</text><text x="600" y="246">04</text>
          <text x="356" y="266">The Solution</text><text x="600" y="266">05</text>
          <text x="356" y="286">The Tidy Vault System</text><text x="600" y="286">06</text>
          <text x="356" y="306">The Software</text><text x="600" y="306">08</text>
          <text x="356" y="326">Installation and Training</text><text x="600" y="326">10</text>
          <text x="356" y="346">Get Started</text><text x="600" y="346">12</text>
        </g>
        <g stroke="var(--rule)" stroke-width="1">
          <line x1="356" y1="232" x2="612" y2="232"/><line x1="356" y1="252" x2="612" y2="252"/>
          <line x1="356" y1="272" x2="612" y2="272"/><line x1="356" y1="292" x2="612" y2="292"/>
          <line x1="356" y1="312" x2="612" y2="312"/><line x1="356" y1="332" x2="612" y2="332"/>
          <line x1="356" y1="352" x2="612" y2="352"/>
        </g>
        <rect x="318" y="0" width="2" height="420" fill="url(#g-fold)"/>
      </symbol>

      <!-- Problem / solution -->
      <symbol id="s-problem" viewBox="0 0 640 420">
        <rect width="640" height="420" fill="#fff"/>
        <rect x="0" y="0" width="320" height="220" fill="url(#g-boxes)" role="img" aria-label="Photo of a room crowded with paper file boxes"/>
        <rect x="0" y="180" width="130" height="40" fill="var(--red)"/>
        <text x="14" y="210" class="h" font-size="26" fill="#fff">PROBLEM</text>
        <g class="b" font-size="8.5" fill="var(--ink)">
          <rect x="30" y="242" width="7" height="7" fill="var(--red)"/><text x="44" y="249">Paper files taking over rooms</text>
          <rect x="30" y="264" width="7" height="7" fill="var(--red)"/><text x="44" y="271">Lost records and wasted hours</text>
          <rect x="30" y="286" width="7" height="7" fill="var(--red)"/><text x="44" y="293">Risk of water and fire damage</text>
          <rect x="30" y="308" width="7" height="7" fill="var(--red)"/><text x="44" y="315">No clear retention schedule in place</text>
          <rect x="30" y="330" width="7" height="7" fill="var(--red)"/><text x="44" y="337">Staff time spent searching for files</text>
          <rect x="30" y="352" width="7" height="7" fill="var(--red)"/><text x="44" y="359">Compliance gaps during audits</text>
          <rect x="30" y="374" width="7" height="7" fill="var(--red)"/><text x="44" y="381">Poor access control</text>
        </g>
        <rect x="320" y="0" width="320" height="420" fill="var(--blue)"/>
        <rect x="320" y="0" width="150" height="150" fill="url(#g-crates)" role="img" aria-label="Photo of coloured archive crates"/>
        <rect x="470" y="0" width="130" height="40" fill="var(--blue-dark)"/>
        <text x="480" y="30" class="h" font-size="26" fill="#fff">SOLUTION</text>
        <g class="b" font-size="7.5" fill="#fff">
          <text x="480" y="62">A secure, tidy archive built to fit</text>
          <text x="480" y="74">your school, your space and your</text>
          <text x="480" y="86">records. We design, supply and</text>
          <text x="480" y="98">install every part of the system.</text>
        </g>
        <g class="bb" font-size="8" fill="#fff">
          <text x="340" y="180">Secure Storage System</text>
          <text x="340" y="196">Records Management Software</text>
          <text x="340" y="212">Training and Support</text>
        </g>
        <text x="336" y="266" class="h" font-size="40" fill="#fff">&#8220;</text>
        <g class="b" font-size="8" fill="#fff">
          <text x="360" y="256">Our records are finally in one safe place and</text>
          <text x="360" y="268">staff can find any file in minutes.</text>
          <text x="360" y="286" font-style="normal">Business Manager, Victorian school</text>
        </g>
        <rect x="470" y="300" width="150" height="100" fill="#f3f3f3" opacity=".95" role="img" aria-label="Illustration of the mascots with archive boxes"/>
        <rect x="318" y="0" width="2" height="420" fill="url(#g-fold)"/>
      </symbol>

      <!-- Tidy Vault system -->
      <symbol id="s-system" viewBox="0 0 640 420">
        <rect width="640" height="420" fill="#fff"/>
        <rect x="0" y="0" width="640" height="190" fill="url(#g-crates)" role="img" aria-label="Photo of blue, red and yellow archive crates on shelves"/>
        <rect x="0" y="130" width="170" height="80" fill="var(--blue)"/>
        <text x="14" y="162" class="h" font-size="24" fill="#fff">THE TIDY VAULT</text>
        <text x="14" y="196" class="h" font-size="24" fill="#fff">SYSTEM</text>
        <circle cx="520" cy="120" r="40" fill="#fff"/>
        <circle cx="520" cy="120" r="32" fill="var(--blue)"/>
        <text x="20" y="232" class="hm" font-size="11" fill="var(--ink)">ONSITE STORAGE SYSTEM - TIDY VAULT</text>
        <g class="b" font-size="7.5" fill="var(--ink)">
          <text x="20" y="248">A modular system of lockers and crates that keeps every</text>
          <text x="20" y="259">record secure, labelled and easy to reach on your site.</text>
          <text x="20" y="278" class="bb" fill="var(--blue)">Every system is made to suit your school</text>
        </g>
        <g class="b" font-size="7.5" fill="var(--ink)">
          <rect x="20" y="290" width="6" height="6" fill="var(--blue)"/><text x="32" y="296">Lockable steel lockers</text>
          <rect x="20" y="306" width="6" height="6" fill="var(--blue)"/><text x="32" y="312">Colour coded crates</text>
          <rect x="20" y="322" width="6" height="6" fill="var(--blue)"/><text x="32" y="328">Barcode ready labels</text>
          <rect x="20" y="338" width="6" height="6" fill="var(--blue)"/><text x="32" y="344">Fire rated options</text>
          <rect x="170" y="290" width="6" height="6" fill="var(--blue)"/><text x="182" y="296">Custom room layout</text>
          <rect x="170" y="306" width="6" height="6" fill="var(--blue)"/><text x="182" y="312">Flexible expansion</text>
          <rect x="170" y="322" width="6" height="6" fill="var(--blue)"/><text x="182" y="328">Fast retrieval</text>
          <rect x="170" y="338" width="6" height="6" fill="var(--blue)"/><text x="182" y="344">Full install</text>
        </g>
        <rect x="340" y="205" width="110" height="26" fill="var(--blue)"/>
        <text x="350" y="225" class="h" font-size="16" fill="#fff">TESTIMONIAL</text>
        <text x="340" y="270" class="h" font-size="36" fill="var(--blue)">&#8220;</text>
        <g class="b" font-size="7.5" fill="var(--ink)">
          <text x="362" y="258">The team listened to what we needed and built a</text>
          <text x="362" y="270">system that fits our room perfectly. Our records</text>
          <text x="362" y="282">have never been this organised.</text>
        </g>
        <rect x="340" y="300" width="280" height="90" fill="var(--blue)"/>
        <g class="b" font-size="7.5" fill="#fff">
          <text x="354" y="322">Principal, Melbourne secondary college</text>
          <text x="354" y="340">Installed in term two with no disruption</text>
          <text x="354" y="352">to classes or staff during the school week.</text>
        </g>
        <rect x="318" y="190" width="2" height="230" fill="url(#g-fold)"/>
      </symbol>

      <!-- Software -->
      <symbol id="s-software" viewBox="0 0 640 420">
        <rect width="640" height="420" fill="#fff"/>
        <rect x="0" y="0" width="640" height="210" fill="var(--blue)"/>
        <rect x="20" y="16" width="150" height="34" fill="var(--red)"/>
        <text x="30" y="42" class="h" font-size="22" fill="#fff">THE SOFTWARE</text>
        <g>
          <rect x="30" y="70" width="170" height="106" rx="4" fill="#2b3644"/>
          <rect x="36" y="76" width="158" height="90" fill="#eef3f8" role="img" aria-label="Screenshot of archive search screen"/>
          <rect x="106" y="176" width="30" height="14" fill="#2b3644"/>
          <rect x="235" y="70" width="170" height="106" rx="4" fill="#2b3644"/>
          <rect x="241" y="76" width="158" height="90" fill="#eef3f8" role="img" aria-label="Screenshot of archive dashboard"/>
          <rect x="305" y="176" width="30" height="14" fill="#2b3644"/>
          <rect x="440" y="70" width="170" height="106" rx="4" fill="#2b3644"/>
          <rect x="446" y="76" width="158" height="90" fill="#eef3f8" role="img" aria-label="Screenshot of records report"/>
          <rect x="510" y="176" width="30" height="14" fill="#2b3644"/>
        </g>
        <g class="b" font-size="7.5" fill="var(--ink)">
          <text x="30" y="238">Our software tracks every box, file and crate in your</text>
          <text x="30" y="250">archive. Search, request and return records in a few</text>
          <text x="30" y="262">clicks, with a full history of who accessed what.</text>
        </g>
        <text x="30" y="290" class="hm" font-size="10" fill="var(--blue)">QUICK TRACKING WITH SIMPLE, INTUITIVE SOFTWARE</text>
        <g class="b" font-size="7.5" fill="var(--ink)">
          <rect x="30" y="304" width="6" height="6" fill="var(--red)"/><text x="42" y="310">Search records instantly</text>
          <rect x="30" y="320" width="6" height="6" fill="var(--red)"/><text x="42" y="326">Track file movement</text>
          <rect x="30" y="336" width="6" height="6" fill="var(--red)"/><text x="42" y="342">Set retention dates</text>
          <rect x="180" y="304" width="6" height="6" fill="var(--red)"/><text x="192" y="310">Secure user access</text>
          <rect x="180" y="320" width="6" height="6" fill="var(--red)"/><text x="192" y="326">Audit ready reports</text>
          <rect x="180" y="336" width="6" height="6" fill="var(--red)"/><text x="192" y="342">Cloud based backup</text>
        </g>
        <rect x="340" y="230" width="280" height="120" fill="var(--blue)"/>
        <g class="b" font-size="7.5" fill="#fff">
          <text x="354" y="254">Built with schools in mind, the software works</text>
          <text x="354" y="266">alongside your storage system so every record</text>
          <text x="354" y="278">has a clear home and a clear owner.</text>
        </g>
        <rect x="520" y="286" width="90" height="110" fill="#d9e8f5" role="img" aria-label="Illustration of a mascot pointing at a screen"/>
        <rect x="318" y="210" width="2" height="210" fill="url(#g-fold)"/>
      </symbol>
    </defs>
  </svg>

  <!-- Stage overview -->
  <svg class="thumb" style="left:140px;top:60px" viewBox="0 0 640 420"><use href="#s-cover"/></svg>
  <svg class="thumb" style="left:640px;top:60px" viewBox="0 0 640 420"><use href="#s-toc"/></svg>
  <svg class="thumb" style="left:140px;top:500px" viewBox="0 0 640 420"><use href="#s-problem"/></svg>
  <svg class="thumb" style="left:640px;top:500px" viewBox="0 0 640 420"><use href="#s-system"/></svg>
  <svg class="thumb" style="left:140px;top:940px" viewBox="0 0 640 420"><use href="#s-software"/></svg>
  <svg class="thumb" style="left:640px;top:940px" viewBox="0 0 640 420"><use href="#s-cover"/></svg>

  <!-- Full spreads -->
  <svg class="spread" style="top:1370px" viewBox="0 0 640 420"><use href="#s-cover"/></svg>
  <svg class="spread" style="top:1830px" viewBox="0 0 640 420"><use href="#s-toc"/></svg>
  <svg class="spread" style="top:2290px" viewBox="0 0 640 420"><use href="#s-problem"/></svg>
  <svg class="spread" style="top:2750px" viewBox="0 0 640 420"><use href="#s-system"/></svg>
  <svg class="spread" style="top:3210px" viewBox="0 0 640 420"><use href="#s-software"/></svg>
</div>
</body>
</html>
```